Kestrel Valley Alpine Riders Society needs a business card design

We need a business card design for our newly incorporated KVARS. We are helping the NZ Chinese community, as well as everyone else, to organise ski & snowboarding trips, training, and equipments. The design should be creative, energetic, young and vibrant.

Industry/Entity Type

Social Club

Contact Information for Business Card

Logo; Kestrel Valley Alpine Riders Society; Name: Oliver Brandt; Position: President; Address: 42 Marwick Rd, Epsom, Auckland 1051; Mobile: 020 7826 1957; Email: oliver@kvars-club.example; Web: www.kvars-club.example

Requirements
Must have
• 1, The text "Kestrel Valley Alpine Riders Society" should be put together with the supplied logo file to form a new complete logo combination.
• 2, Final design files should be in Adobe Illustrator format and all text must be editable.
Nice to have
• two or three colours

```html
<!DOCTYPE html>
<html lang="en">
<head>
<meta charset="utf-8">
<title>Kestrel Valley Alpine Riders Society – Business Card</title>
<link href="https://fonts.googleapis.com/css2?family=Open+Sans:wght@400;600;800&family=Roboto+Condensed:wght@700&display=swap" rel="stylesheet">
<style>
  :root {
    --navy: #0b2a8c;
    --navy-deep: #08206f;
    --sky: #2f8fe0;
    --sky-light: #4aa8f0;
    --paper: #ffffff;
    --ink: #333a45;
    --backdrop: #eceef2;
  }
  * { box-sizing: border-box; margin: 0; padding: 0; }
  html, body { width: 1200px; height: 900px; overflow: hidden; }
  body {
    background: var(--backdrop);
    font-family: "Open Sans", Arial, sans-serif;
    position: relative;
  }
  .card {
    position: absolute;
    left: 264px;
    width: 672px;
    height: 384px;
    overflow: hidden;
    box-shadow: 0 6px 18px rgba(0,0,0,0.18);
  }
  /* Front */
  .card-front { top: 48px; background: var(--navy); }
  .front-lockup {
    position: absolute; inset: 0;
    display: flex; flex-direction: column; align-items: center; justify-content: center;
  }
  .brand-mark {
    display: flex; align-items: center; gap: 14px;
    font-family: "Open Sans", Arial, sans-serif;
    font-weight: 800;
    letter-spacing: 2px;
  }
  .brand-mark .dot { border-radius: 50%; display: block; }
  .card-front .brand-mark { color: var(--paper); font-size: 62px; }
  .card-front .brand-mark .dot { width: 44px; height: 44px; background: var(--sky-light); }
  .front-name {
    margin-top: 10px;
    font-family: "Roboto Condensed", "Arial Narrow", sans-serif;
    font-weight: 700;
    font-size: 58px;
    line-height: 1;
    color: var(--sky-light);
  }
  .front-sub {
    margin-top: 6px;
    font-family: "Roboto Condensed", "Arial Narrow", sans-serif;
    font-weight: 700;
    font-size: 22px;
    letter-spacing: 1px;
    color: var(--paper);
  }
  /* Back */
  .card-back { top: 468px; background: var(--paper); }
  .back-wave { position: absolute; left: 0; top: 0; width: 672px; height: 384px; }
  .back-logo { position: absolute; right: 38px; top: 36px; }
  .card-back .brand-mark { color: var(--navy); font-size: 50px; }
  .card-back .brand-mark .dot { width: 34px; height: 34px; background: var(--sky); }
  .person { position: absolute; left: 50px; top: 48px; }
  .person-name {
    font-weight: 600; font-size: 24px; color: var(--sky); letter-spacing: 0.5px;
  }
  .person-role { font-size: 15px; color: var(--ink); margin-top: 2px; }
  .contacts { position: absolute; left: 50px; top: 128px; list-style: none; }
  .contacts li {
    display: flex; align-items: center; gap: 9px;
    font-size: 15px; color: var(--ink); line-height: 24px;
  }
  .contacts svg { width: 14px; height: 14px; fill: var(--sky); flex: none; }
  .address {
    position: absolute; left: 73px; top: 214px;
    font-size: 15px; line-height: 22px; color: var(--ink); font-style: normal;
  }
</style>
</head>
<body>

<section class="card card-front" aria-label="Card front">
  <div class="front-lockup">
    <div class="brand-mark"><span class="dot"></span>KVARS</div>
    <div class="front-name">Kestrel Valley</div>
    <div class="front-sub">ALPINE RIDERS SOCIETY</div>
  </div>
</section>

<section class="card card-back" aria-label="Card back">
  <svg class="back-wave" viewBox="0 0 672 384" aria-hidden="true">
    <path d="M0 280 C200 330 430 292 600 180 C440 300 220 348 0 308 Z" fill="var(--sky)"/>
    <path d="M0 312 C210 350 440 300 672 150 L672 384 L0 384 Z" fill="var(--navy)"/>
  </svg>

  <div class="back-logo">
    <div class="brand-mark"><span class="dot"></span>KVARS</div>
  </div>

  <div class="person">
    <div class="person-name">OLIVER BRANDT</div>
    <div class="person-role">President</div>
  </div>

  <ul class="contacts">
    <li>
      <svg viewBox="0 0 24 24"><path d="M6.6 10.8a15.1 15.1 0 0 0 6.6 6.6l2.2-2.2a1 1 0 0 1 1-.25 11.4 11.4 0 0 0 3.6.57 1 1 0 0 1 1 1V20a1 1 0 0 1-1 1A17 17 0 0 1 3 4a1 1 0 0 1 1-1h3.5a1 1 0 0 1 1 1c0 1.25.2 2.45.57 3.57a1 1 0 0 1-.25 1Z"/></svg>
      020 7826 1957
    </li>
    <li>
      <svg viewBox="0 0 24 24"><path d="M2 5h20v14H2Z M3.5 6.5 12 13l8.5-6.5" fill="var(--sky)"/><path d="M3.5 6.5 12 13l8.5-6.5" fill="none" stroke="#fff" stroke-width="1.6"/></svg>
      oliver@kvars-club.example
    </li>
    <li>
      <svg viewBox="0 0 24 24"><circle cx="12" cy="12" r="10"/><path d="M2 12h20M12 2c3 3 3 17 0 20M12 2c-3 3-3 17 0 20" fill="none" stroke="#fff" stroke-width="1.4"/></svg>
      www.kvars-club.example
    </li>
  </ul>

  <address class="address">42 Marwick Rd,<br>Epsom, Auckland 1051</address>
</section>

</body>
</html>
```